Business Card Design for Portrait photography professional

We are a small company specializing in portrait photography (weddings, family, couples, children, newborn, pregnant, etc.) Occasionally we do business portraits too and do some other type of photography. We need a business card which would fit into the same look and feel as our website theme (lumvika.com - under construction currently).
Our target customer base lies within mid- to upmarket. We want our business cards to convey a feeling of quality, solidness and a bit luxury.
Design should be universal and usable on 85mmx55mm, 90mmx50mm and 90mmx55mm
one extra file (PSD of a website didn't fit into the allowed updoad, therefore has put it into my filecrate: https://www.filecrate-example.net/s/qt7wk2rbvx9dmhe/website%20theme%20PSD.psd)

Target Market(s)

mostly private people, 25-60 years old, mostly well established.

Industry/Entity Type

Portrait Photography

Requirements
Must have
• 2 sided design (print on both sides of the business card).
Must include:
business name, logo, URL (lumvika.no) , employee name, email address, and phone number.
Colorscheme of the website lumvika.no / lumvika.com

```html
<!DOCTYPE html>
<html lang="en">
<head>
<meta charset="utf-8">
<title>Lumvika Portraits – Business Card Front and Back</title>
<link href="https://fonts.googleapis.com/css2?family=Cinzel:wght@400;600&display=swap" rel="stylesheet">
<style>
  :root {
    --board-light: #f7f9f8;
    --board-mid: #e3e8e7;
    --label-grey: #6f7573;
    --ivory: #f6f1e4;
    --sky-light: #e6f0f8;
    --sky-mid: #c9dcec;
    --skin-soft: #e9c9bd;
    --sage-dark: #59654d;
    --sage-mid: #7f8a6a;
    --sage-light: #b4bd9b;
    --card-shadow: rgba(0, 0, 0, 0.45);
    --text-lift: rgba(60, 80, 100, 0.45);
  }
  html, body {
    margin: 0;
    padding: 0;
    width: 1200px;
    height: 1000px;
    overflow: hidden;
  }
  body {
    position: relative;
    background: linear-gradient(135deg, var(--board-mid) 0%, var(--board-light) 45%, var(--board-mid) 100%);
    font-family: "Cinzel", "Times New Roman", serif;
  }
  .side-label {
    position: absolute;
    color: var(--label-grey);
    font-size: 30px;
    font-weight: 600;
    letter-spacing: 9px;
    line-height: 36px;
  }
  .side-label--front { left: 788px; top: 36px; }
  .side-label--back { left: 285px; top: 922px; }

  .card {
    position: absolute;
    box-shadow: 2px 3px 6px var(--card-shadow);
    overflow: hidden;
    color: var(--ivory);
    text-align: center;
  }
  .card--front {
    left: 40px; top: 40px; width: 722px; height: 440px;
  }
  .card--back {
    left: 437px; top: 510px; width: 723px; height: 443px;
    background: linear-gradient(125deg, var(--sage-dark) 0%, var(--sage-mid) 50%, var(--sage-light) 100%);
  }
  .portrait-photo {
    position: absolute; inset: 0;
    background:
      radial-gradient(ellipse 230px 260px at 590px 250px, var(--skin-soft) 0%, rgba(233,201,189,0.6) 45%, rgba(233,201,189,0) 100%),
      linear-gradient(90deg, var(--sky-light) 0%, var(--sky-mid) 100%);
  }
  .brand-mark {
    position: absolute;
    display: flex;
    align-items: center;
    justify-content: center;
    border: 3px solid var(--ivory);
    border-radius: 50%;
    box-sizing: border-box;
  }
  .card--front .brand-mark { left: 270px; top: 125px; width: 182px; height: 182px; }
  .card--back .brand-mark { left: 250px; top: 42px; width: 222px; height: 222px; }
  .brand-name {
    font-weight: 600;
    letter-spacing: 2px;
  }
  .card--front .brand-name { font-size: 24px; }
  .card--back .brand-name { font-size: 30px; }

  .business-block { position: absolute; left: 0; right: 0; }
  .card--front .business-block {
    top: 314px; left: 0; right: auto; width: 722px;
    margin-left: -82px;
    text-shadow: 0 1px 2px var(--text-lift);
  }
  .card--back .business-block { top: 284px; }
  .business-name { margin: 0; letter-spacing: 1px; font-weight: 600; line-height: 1.2; }
  .card--front .business-name { font-size: 13.5px; }
  .card--back .business-name { font-size: 15px; }
  .business-urls { margin: 1px 0 0; letter-spacing: 2px; font-weight: 600; line-height: 1.2; }
  .card--front .business-urls { font-size: 7px; }
  .card--back .business-urls { font-size: 8px; }

  .contact-list {
    position: absolute; left: 0; right: 0; top: 349px;
    margin: 0; padding: 0; list-style: none;
    font-size: 11px; letter-spacing: 3px; line-height: 17px;
  }
</style>
</head>
<body>
  <div class="side-label side-label--front">FRONT</div>
  <div class="side-label side-label--back">BACK</div>

  <section class="card card--front">
    <div class="portrait-photo" role="img" aria-label="Soft studio portrait of a young child in a plaid cap against a pale blue background"></div>
    <div class="brand-mark"><span class="brand-name">LUMVIKA</span></div>
    <div class="business-block">
      <p class="business-name">LUMVIKA PORTRAITS</p>
      <p class="business-urls">LUMVIKA.NO - LUMVIKA.COM</p>
    </div>
  </section>

  <section class="card card--back">
    <div class="brand-mark"><span class="brand-name">LUMVIKA</span></div>
    <div class="business-block">
      <p class="business-name">LUMVIKA PORTRAITS</p>
      <p class="business-urls">LUMVIKA.NO - LUMVIKA.COM</p>
    </div>
    <ul class="contact-list">
      <li>EMPLOYEE NAME</li>
      <li>EMPLOYEE@MAILHAVEN.COM</li>
      <li>CALL: (000)-000-0000</li>
    </ul>
  </section>
</body>
</html>
```